Garlic Farm for Farm Sales/Restaurant sales

Need a professional, but appealing to agriculture world. We are selling 27 kinds of Organic Garlic from a farm in Simla,CO. I have uploaded logo and business information-we are going to need a template, because I will need to use it for four separate people.
-We are trying to appeal to Farm to table restaurants
-As well as growers/farmers

Target Market(s)

Agriculture Sales/Restaurants-Organic

Industry/Entity Type

Agriculture

Contact Information for Business Card

Want it to look more unique then your average orbel mart card- I want it to look amazing

Font styles to use
Sans Serif

Colors
0455a3
ec1f27
fbed22
ffffff

Requirements
Must have
• Just be creative
Nice to have
• Colorful
Should not have
• plain

```html
<!DOCTYPE html>
<html lang="en">
<head>
<meta charset="utf-8">
<title>Prairie Crest Garlic – Business Card</title>
<link rel="stylesheet" href="https://fonts.googleapis.com/css2?family=Open+Sans:wght@400;600;700&display=swap">
<style>
  :root {
    --card-red: #c41f2e;
    --navy: #1b2f6b;
    --white: #ffffff;
    --stage: #e6e6e8;
    --shadow: rgba(0, 0, 0, 0.18);
  }
  * { box-sizing: border-box; margin: 0; padding: 0; }
  html, body {
    width: 1200px; height: 880px; overflow: hidden;
    background: var(--stage);
    font-family: "Open Sans", sans-serif;
  }
  .canvas {
    position: relative; width: 1200px; height: 880px;
  }
  .card {
    position: absolute; left: 280px;
    width: 640px; height: 366px;
    border-radius: 4px; overflow: hidden;
    box-shadow: 0 6px 18px var(--shadow);
  }
  .card--front { top: 50px; background: var(--card-red); }
  .card--back { top: 464px; background: var(--white); }

  /* Front */
  .front-brand {
    position: absolute; inset: 0;
    display: flex; flex-direction: column; align-items: center; justify-content: center;
    color: var(--white); text-align: center;
  }
  .front-brand__name {
    font-size: 46px; font-weight: 700; letter-spacing: 0.5px; line-height: 1.05;
  }
  .front-brand__tagline {
    font-size: 20px; font-weight: 700; margin-top: 6px; letter-spacing: 2px;
  }
  .front-brand__web {
    font-size: 17px; font-weight: 400; margin-top: 22px; letter-spacing: 0.5px;
  }

  /* Back */
  .back-swoop { position: absolute; inset: 0; }
  .back-brand {
    position: absolute; left: 34px; top: 120px; width: 250px;
    display: flex; align-items: center; gap: 12px;
    color: var(--navy);
  }
  .back-brand__dot {
    flex: none; width: 40px; height: 40px; border-radius: 50%;
    background: var(--card-red);
  }
  .back-brand__name {
    font-size: 30px; font-weight: 700; line-height: 1.05;
  }
  .back-brand__name span { display: block; font-size: 16px; letter-spacing: 1.5px; margin-top: 4px; }

  .contact {
    position: absolute; left: 390px; top: 48px; width: 230px;
    color: var(--white);
  }
  .contact__name { font-size: 24px; font-weight: 700; letter-spacing: 0.5px; }
  .contact__address { font-size: 14px; line-height: 1.35; margin-top: 34px; }
  .contact__list { list-style: none; margin-top: 16px; }
  .contact__item {
    display: flex; align-items: center; gap: 8px;
    font-size: 14px; line-height: 1.5;
  }
  .contact__icon { width: 14px; height: 14px; flex: none; }
  .social {
    display: flex; gap: 6px; margin-top: 16px;
  }
  .social__box {
    width: 20px; height: 20px; background: var(--white); border-radius: 2px;
  }
</style>
</head>
<body>
<main class="canvas">

  <section class="card card--front" aria-label="Business card front">
    <div class="front-brand">
      <div class="front-brand__name">Prairie Crest</div>
      <div class="front-brand__tagline">GOURMET GARLIC</div>
      <div class="front-brand__web">PCGarlic.com</div>
    </div>
  </section>

  <section class="card card--back" aria-label="Business card back">
    <svg class="back-swoop" width="640" height="366" viewBox="0 0 640 366" aria-hidden="true">
      <path d="M236 0 C 290 120, 395 200, 412 366 L 640 366 L 640 0 Z" fill="var(--navy)"/>
      <path d="M252 0 C 306 118, 416 196, 436 366 L 640 366 L 640 0 Z" fill="var(--white)"/>
      <path d="M256 0 C 310 118, 420 196, 440 366 L 640 366 L 640 0 Z" fill="var(--card-red)"/>
    </svg>

    <div class="back-brand">
      <span class="back-brand__dot"></span>
      <div class="back-brand__name">Prairie Crest<span>GOURMET GARLIC</span></div>
    </div>

    <div class="contact">
      <div class="contact__name">Dana Wells</div>
      <div class="contact__address">P.O. Box 48 Aldon,<br>CO 80999</div>
      <ul class="contact__list">
        <li class="contact__item">
          <svg class="contact__icon" viewBox="0 0 16 16" aria-hidden="true"><rect width="16" height="16" rx="2" fill="var(--white)"/><path d="M4.5 3.5 L6.5 3.5 L7.3 6 L6 7 C6.7 8.4 7.6 9.3 9 10 L10 8.7 L12.5 9.5 L12.5 11.5 C8 11.8 4.2 8 4.5 3.5Z" fill="var(--card-red)"/></svg>
          555-014-2286
        </li>
        <li class="contact__item">
          <svg class="contact__icon" viewBox="0 0 16 16" aria-hidden="true"><rect width="16" height="16" rx="2" fill="var(--white)"/><rect x="3" y="4.5" width="10" height="7" fill="none" stroke="var(--card-red)" stroke-width="1.3"/><path d="M3 4.5 L8 8.5 L13 4.5" fill="none" stroke="var(--card-red)" stroke-width="1.3"/></svg>
          Dana@PCGarlic.com
        </li>
        <li class="contact__item">
          <svg class="contact__icon" viewBox="0 0 16 16" aria-hidden="true"><circle cx="8" cy="8" r="7.5" fill="var(--white)"/><circle cx="8" cy="8" r="5" fill="none" stroke="var(--card-red)" stroke-width="1.1"/><ellipse cx="8" cy="8" rx="2.2" ry="5" fill="none" stroke="var(--card-red)" stroke-width="1.1"/><path d="M3 8 H13" stroke="var(--card-red)" stroke-width="1.1"/></svg>
          PCGarlic.com
        </li>
      </ul>
      <div class="social" aria-label="Social channels">
        <span class="social__box"></span>
        <span class="social__box"></span>
        <span class="social__box"></span>
        <span class="social__box"></span>
      </div>
    </div>
  </section>

</main>
</body>
</html>
```